Guaranteed Job - Sleek Sexy Business Card UV Spot

Im looking for a sleek and sexy business card, that resembles elite or VIP status status.
our business is corinvale.example
you can view our products on there, but our main audience for handing out our cards will be for people in the hospitality industry, so it will need to impress high management and CEO of hotels and restaurants, bars, clubs etc...
the card features will have UV spot on both sides, 400gsm stock. standard size.
Artwork should be 86 x 54mm + 2mm bleed = 90 x 58mm
it should have a nice "unique" uv spot pattern that highlights the card, not a repeated pattern, theres no originality there, and it will be disregarded.
The written material will be:
Corin Vale Hospitality College (logo)
Tobin Marsh
Director
Phone: 1300 615 737
Mobile: 0455 817 296
Email: info@corinvale.example
website: www.corinvale.example
I'm looking for originality here, i don't want just a simple stock card, want something that has a wow factor for people.
You will find the logo attached. you may invert the white to black words to suit the background as you please.
thank you and good luck
As a side note, ive received a lot of proposals, im too busy to give feedback to each and every one, so if i havent provided feedback for your design within 24 hours, then consider it not acceptable, and you could resubmit another design.
So far i have not seen any design that stood out for me, they all seem pretty generic. there nothing thats unique, i would figure for the amount that im offering, that people would put some more effort and creativity into the design.
so far over 200 designs submitted, and nothing i have seen looks very original, everything looks like a different variation of the same stuff, i said it very clearly i wanted something unique, the only thing that has come close to it so far is this one
Reason: Ive received alot of design concepts and i have reviewed everyone, but i havent had time to give feedback to every single one, only the ones that have interested me, if i havent responded, its because i havent found it good enough.
so far only a few design have been on par with what ive been looking for, an attractive eye popping design.
heres a few of them,
http://files.pixelbazaar.example/design_img/51736/62418/62418_2840915_51736_image.jpg
http://files.pixelbazaar.example/design_img/51736/68254/68254_2841377_51736_image.jpg
theyre, both unique and original, and eye catching, the only thing theyre missing is the sexyness.
if you still think you have some creativity left in your minds, then throw it on here.
Reason: Sorry guys for the delay, I was in a serious accident and out of commission for the past few months, I'm just slowly recovering now, please bare with me as i try to attend to this project, it may take me awhile as I have other projects that are on standby, I'm not 100% at the moment, so im extending the deadline for 2 weeks right now. Thanks for your patience.
Hospitality

```html
<!DOCTYPE html>
<html lang="en">
<head>
<meta charset="utf-8">
<title>Corin Vale Hospitality College – Business Card</title>
<link rel="stylesheet" href="https://fonts.googleapis.com/css2?family=Open+Sans:wght@400;600;700&display=swap">
<style>
  :root {
    --backdrop: #3b3b3d;
    --card: #1c1d20;
    --card-edge: #141517;
    --gloss: #2b2c30;
    --gloss-light: #4a4b50;
    --accent: #4aa3df;
    --text: #f2f2f2;
    --muted: #8a8b90;
  }
  * { box-sizing: border-box; margin: 0; padding: 0; }
  html, body {
    width: 1200px;
    height: 716px;
    overflow: hidden;
    background: var(--backdrop);
    font-family: "Open Sans", Arial, sans-serif;
  }
  .canvas {
    position: relative;
    width: 1200px;
    height: 716px;
  }
  .card {
    position: absolute;
    top: 184px;
    width: 540px;
    height: 348px;
    background: var(--card);
    border: 1px solid var(--card-edge);
    box-shadow: 0 10px 30px rgba(0, 0, 0, 0.45);
    overflow: hidden;
  }
  .card--front { left: 40px; }
  .card--back { left: 620px; }

  /* Front */
  .brand {
    position: absolute;
    left: 34px;
    top: 34px;
    display: flex;
    align-items: center;
    gap: 10px;
  }
  .brand__mark {
    width: 18px;
    height: 18px;
    background: var(--accent);
  }
  .brand__name {
    color: var(--text);
    font-weight: 600;
    font-size: 15px;
    letter-spacing: 0.06em;
    text-transform: uppercase;
    line-height: 1.15;
  }
  .spot-area {
    position: absolute;
    left: 292px;
    top: 60px;
    width: 210px;
    height: 210px;
    background: linear-gradient(135deg, var(--gloss) 0%, var(--gloss-light) 60%, var(--gloss) 100%);
  }
  .person {
    position: absolute;
    left: 110px;
    top: 120px;
  }
  .person__name {
    color: var(--accent);
    font-size: 21px;
    font-weight: 400;
    letter-spacing: 0.03em;
    text-transform: uppercase;
  }
  .person__role {
    color: var(--text);
    font-size: 17px;
    margin-top: 2px;
  }
  .person__mobile {
    display: flex;
    align-items: center;
    gap: 8px;
    color: var(--text);
    font-size: 15px;
    margin-top: 6px;
    margin-left: -22px;
  }
  .contacts {
    position: absolute;
    left: 88px;
    top: 250px;
    list-style: none;
  }
  .contacts__item {
    display: flex;
    align-items: center;
    gap: 10px;
    color: var(--text);
    font-size: 14.5px;
    line-height: 24px;
  }
  .icon { flex: none; }

  /* Back */
  .back-title {
    position: absolute;
    left: 70px;
    top: 96px;
    color: var(--gloss-light);
    font-weight: 700;
    text-transform: uppercase;
  }
  .back-title__line {
    display: block;
    font-size: 58px;
    line-height: 0.98;
    letter-spacing: 0.02em;
  }
  .back-title__sub {
    display: block;
    font-size: 24px;
    letter-spacing: 0.08em;
    margin-top: 6px;
  }
  .back-url {
    position: absolute;
    right: 16px;
    top: 24px;
    writing-mode: vertical-rl;
    font-size: 13px;
    color: var(--muted);
    letter-spacing: 0.04em;
  }
  .back-url__prefix { color: var(--accent); }
</style>
</head>
<body>
<main class="canvas">
  <section class="card card--front" aria-label="Business card front">
    <div class="brand">
      <span class="brand__mark"></span>
      <span class="brand__name">Corin Vale<br>Hospitality College</span>
    </div>

    <div class="spot-area" role="img" aria-label="Large spot UV brand emblem area"></div>

    <div class="person">
      <p class="person__name">Tobin Marsh</p>
      <p class="person__role">Director</p>
      <p class="person__mobile">
        <svg class="icon" width="10" height="14" viewBox="0 0 10 14" aria-hidden="true">
          <rect x="1" y="0.8" width="8" height="12.4" rx="1.5" fill="none" stroke="var(--accent)" stroke-width="1.3"/>
          <line x1="4" y1="11" x2="6" y2="11" stroke="var(--accent)" stroke-width="1.2"/>
        </svg>
        0455 817 296
      </p>
    </div>

    <ul class="contacts">
      <li class="contacts__item">
        <svg class="icon" width="14" height="14" viewBox="0 0 14 14" aria-hidden="true">
          <circle cx="7" cy="7" r="7" fill="var(--accent)"/>
          <path d="M4.3 3.6l1.4-.3.8 1.9-.9.7c.5 1 1.2 1.7 2.2 2.2l.7-.9 1.9.8-.3 1.4c-3.1.2-6-2.7-5.8-5.8z" fill="var(--card)"/>
        </svg>
        1300 615 737
      </li>
      <li class="contacts__item">
        <svg class="icon" width="14" height="14" viewBox="0 0 14 14" aria-hidden="true">
          <rect x="0.5" y="2.5" width="13" height="9" rx="1" fill="var(--accent)"/>
          <path d="M1 3.2l6 4.3 6-4.3" fill="none" stroke="var(--card)" stroke-width="1.1"/>
        </svg>
        info@corinvale.example
      </li>
      <li class="contacts__item">
        <svg class="icon" width="14" height="14" viewBox="0 0 14 14" aria-hidden="true">
          <circle cx="7" cy="7" r="6.3" fill="var(--accent)"/>
          <g fill="none" stroke="var(--card)" stroke-width="0.9">
            <ellipse cx="7" cy="7" rx="2.6" ry="6.2"/>
            <line x1="0.8" y1="7" x2="13.2" y2="7"/>
            <line x1="7" y1="0.8" x2="7" y2="13.2"/>
          </g>
        </svg>
        www.corinvale.example
      </li>
    </ul>
  </section>

  <section class="card card--back" aria-label="Business card back">
    <h1 class="back-title">
      <span class="back-title__line">Corin</span>
      <span class="back-title__line">Vale</span>
      <span class="back-title__sub">Hospitality College</span>
    </h1>
    <p class="back-url"><span class="back-url__prefix">www.</span>corinvale.example</p>
  </section>
</main>
</body>
</html>
```